Dynamic Templates

Our company hosts web stores for our clients. They can set up as many as they wish on our platform, and select from the stock templates we provide. We are looking to increase the number of available stock templates.

Because our users can dynamically control many of the template elements - specifically colors - they have to be flexible and abide by certain rules. These rules are spelled out in the attached documents.

Here are links to two of our most used templates:
http://brivelta.tondashop.example/
http://quillorn.tondashop.example/

Templates need to have a landing page (what you see when first clicking one of the above links). There also needs to be a category page (what you see when clicking any category) and a product detail page (what you see when you arrive at an individual product, where there are various cart options like Buy Now or Request Info).

```html
<!DOCTYPE html>
<html lang="en">
<head>
<meta charset="utf-8">
<title>Tonda Goods — Promotional Products</title>
<link rel="stylesheet" href="https://fonts.googleapis.com/css2?family=Sorts+Mill+Goudy:ital@0;1&family=Arimo:wght@400;700&display=swap">
<style>
  :root{
    --sky:#6cc8ea;
    --sky-deep:#3fb0de;
    --nav-bg:#262626;
    --nav-line:#3a3a3a;
    --nav-text:#ffffff;
    --nav-sub:#b9b9b9;
    --page:#ffffff;
    --ink:#1e1e1e;
    --body-text:#555555;
    --muted:#a9a9a9;
    --rule:#dcdcdc;
    --accent:#e8334f;
    --accent-dark:#c81d3a;
    --footer:#000000;
    --footer-text:#d6d6d6;
    --footer-head:#bdbdbd;
    --footer-rule:#555555;
  }
  *{box-sizing:border-box;margin:0;padding:0}
  html,body{width:992px;height:1200px;overflow:hidden;background:var(--page)}
  body{position:relative;font-family:"Sorts Mill Goudy",Georgia,serif;color:var(--ink)}

  .masthead{position:absolute;left:0;top:0;width:992px;height:62px;
    background:linear-gradient(180deg,var(--sky) 0%,var(--sky-deep) 100%)}
  .masthead-art{position:absolute;right:0;top:0;width:560px;height:62px;
    background:radial-gradient(ellipse at 60% 110%,#e9f7fc 0 30%,transparent 31%),
               radial-gradient(ellipse at 85% 120%,#f4fbfd 0 28%,transparent 29%),
               linear-gradient(90deg,transparent,#9ad8ee)}
  .brand-name{position:absolute;left:126px;top:14px;font-family:"Sorts Mill Goudy",Georgia,serif;
    font-weight:400;font-size:24px;line-height:28px;color:#ffffff}

  .main-nav{position:absolute;left:0;top:62px;width:992px;height:70px;background:var(--nav-bg)}
  .main-nav ul{list-style:none;position:absolute;left:126px;top:13px;display:flex}
  .main-nav li{width:135px;height:44px;padding-left:17px;border-left:1px solid var(--nav-line)}
  .main-nav .nav-title{display:block;font-style:italic;font-size:18px;color:var(--nav-text);line-height:22px}
  .main-nav .nav-sub{display:block;font-family:"Arimo",Arial,sans-serif;font-size:10px;color:var(--nav-sub);margin-top:4px}

  .showcase{position:absolute;top:168px;left:0;width:992px;height:240px}
  .item{position:absolute;top:0;height:238px}
  .item-photo{position:absolute;right:0;top:0;height:238px}
  .item-label{position:absolute;left:4px;bottom:4px;writing-mode:vertical-rl;transform:rotate(180deg);
    font-family:"Arimo",Arial,sans-serif;font-size:10px;letter-spacing:2px;color:#c9c9c9}
  .item-1{left:126px;width:182px}
  .item-2{left:326px;width:172px}
  .item-3{left:506px;width:183px}
  .item-4{left:698px;width:180px}
  .item-1 .item-photo{width:162px;background:linear-gradient(135deg,#2b2e86,#101a55 60%,#c9cbd8)}
  .item-2 .item-photo{width:150px;background:linear-gradient(180deg,#dccfa9 0%,#cbbd93 55%,#222 62%,#333 100%)}
  .item-3 .item-photo{width:183px;background:linear-gradient(160deg,#222 0%,#3a3a3a 45%,#c62b2b 70%,#e8e8e8 100%)}
  .item-4 .item-photo{width:140px;background:linear-gradient(180deg,#fff 0%,#b8733a 30%,#d39a55 50%,#b7d57a 75%,#9fc15a 100%)}

  .welcome{position:absolute;left:126px;top:451px;width:752px}
  .welcome .rule{height:5px;background:var(--rule)}
  .welcome-row{display:flex;justify-content:space-between;align-items:center;height:58px}
  .welcome h1{font-weight:400;font-size:27px;color:var(--ink);font-style:italic}
  .welcome h1 .soft{color:var(--muted);font-size:30px}
  .btn-shop{display:inline-block;width:156px;height:33px;border-radius:7px;
    background:linear-gradient(180deg,#f2566f,var(--accent-dark));color:#fff;font-style:italic;
    font-size:20px;line-height:33px;text-align:center;text-decoration:none}

  .intro{position:absolute;left:126px;top:528px;width:722px;font-style:italic;font-size:16px;line-height:19px;color:var(--body-text);letter-spacing:.3px}
  .intro p{margin-bottom:19px}

  .footer-edge{position:absolute;left:0;top:790px;width:992px;height:125px}
  .site-footer{position:absolute;left:0;top:912px;width:992px;height:288px;background:var(--footer)}
  .foot-col{position:absolute;top:26px;width:170px}
  .foot-col h2{font-weight:400;font-style:italic;font-size:20px;color:var(--footer-head);padding-bottom:6px;border-bottom:1px dashed var(--footer-rule)}
  .foot-col ul{list-style:none}
  .foot-col li{font-family:"Arimo",Arial,sans-serif;font-weight:700;font-size:10.5px;letter-spacing:.4px;color:var(--footer-text);
    height:28px;line-height:27px;border-bottom:1px dashed var(--footer-rule)}
  .col-a{left:126px}.col-b{left:320px}.col-c{left:515px}.col-d{left:708px}
  .search-box{display:block;width:124px;height:17px;background:#fff;border:0;margin-top:9px}
  .search-line{border-bottom:1px dashed var(--footer-rule);width:170px;margin-top:-9px;height:9px}
  .search-go{font-family:"Arimo",Arial,sans-serif;font-size:10.5px;color:var(--footer-text);margin-top:4px}
  .contact-head{margin-top:46px}
  .copyright{position:absolute;left:126px;top:267px;font-family:"Arimo",Arial,sans-serif;font-size:10px;color:#6a6a6a}
</style>
</head>
<body>
  <header class="masthead">
    <div class="masthead-art" role="img" aria-label="Decorative bubbles and concentric circle pattern"></div>
    <span class="brand-name">Tonda Goods</span>
  </header>

  <nav class="main-nav">
    <ul>
      <li><span class="nav-title">Home</span><span class="nav-sub">we're at home</span></li>
      <li><span class="nav-title">About</span><span class="nav-sub">all about us</span></li>
      <li><span class="nav-title">Shopping</span><span class="nav-sub">our products</span></li>
      <li><span class="nav-title">News</span><span class="nav-sub">latest news</span></li>
      <li><span class="nav-title">Contact</span><span class="nav-sub">get in touch</span></li>
    </ul>
  </nav>

  <section class="showcase">
    <div class="item item-1"><div class="item-photo" role="img" aria-label="Product photo: blue branded desk gadget"></div><span class="item-label">SHOPPING ITEM NAME</span></div>
    <div class="item item-2"><div class="item-photo" role="img" aria-label="Product photo: two-tone branded baseball cap"></div><span class="item-label">SHOPPING ITEM NAME</span></div>
    <div class="item item-3"><div class="item-photo" role="img" aria-label="Product photo: black branded first aid kit with contents"></div></div>
    <div class="item item-4"><div class="item-photo" role="img" aria-label="Product photo: green vase with dried flowers"></div><span class="item-label">SHOPPING ITEM NAME</span></div>
  </section>

  <section class="welcome">
    <div class="rule"></div>
    <div class="welcome-row">
      <h1>Welcome To The Future of <span class="soft">Promotional Products!</span></h1>
      <a class="btn-shop" href="#">Start Shopping</a>
    </div>
    <div class="rule"></div>
  </section>

  <section class="intro">
    <p>Gone are the days of searching through dog-eared catalogs or trying to make sense of complicated product websites.</p>
    <p>We do the work for you! We've taken only the very best and most current products and placed them in easy-to-use categories designed for your needs. Take a look at our selection - quality products at excellent prices.</p>
    <p>Enjoy This Amazing New Resource</p>
    <p>We know you don't have time to waste; so we've cut to the chase and made it simple! But keep in mind, we do have access to over a million products - so if you don't see what you're looking for or have a special theme or request, let us know - we'll find it!</p>
  </section>

  <svg class="footer-edge" width="992" height="125" viewBox="0 0 992 125" role="img" aria-label="Grey paint splash edge above the footer">
    <defs>
      <linearGradient id="edge-fade" x1="0" y1="0" x2="0" y2="1">
        <stop offset="0" stop-color="#ffffff"/>
        <stop offset="1" stop-color="#d2d2d2"/>
      </linearGradient>
    </defs>
    <path d="M0 70 C80 40 150 60 230 45 C330 30 420 55 520 40 C620 28 720 50 820 35 C890 28 950 40 992 30 L992 125 L0 125 Z" fill="url(#edge-fade)"/>
    <path d="M0 105 C120 80 230 110 360 92 C480 76 560 104 680 90 C790 78 880 96 992 86 L992 125 L0 125 Z" fill="#000"/>
  </svg>

  <footer class="site-footer">
    <div class="foot-col col-a">
      <h2>Shop By Category</h2>
      <ul><li>Apparel</li><li>Bags &amp; Totes</li><li>Computer</li><li>Eco Friendly</li><li>Food, Candy &amp; Drink</li><li>Tools &amp; Hardware</li></ul>
    </div>
    <div class="foot-col col-b">
      <h2>...</h2>
      <ul><li>Auto</li><li>Clocks &amp; Watches</li><li>Electronics</li><li>Games</li><li>Giftsets</li><li>Keychains</li></ul>
    </div>
    <div class="foot-col col-c">
      <h2>Shop By Price</h2>
      <ul><li>Under $5</li><li>$5 - $10</li><li>$10 - $20</li><li>$20 - $50</li><li>$50 - $100</li><li>$100 - $200</li></ul>
    </div>
    <div class="foot-col col-d">
      <h2 style="border-bottom:0">Quick Search</h2>
      <input class="search-box" type="text" aria-label="Quick search">
      <div class="search-line"></div>
      <div class="search-go">Go</div>
      <h2 class="contact-head">Contact Us</h2>
      <ul><li>info@tondagoods.example</li><li>www.tondagoods.example</li></ul>
    </div>
    <p class="copyright">Copyright © 2010 . TondaGoods.example V3 . All Rights Reserved.</p>
  </footer>
</body>
</html>
```